Lumora business card for a plastic surgeon

we need a business card for plastic surgeons that work on a clinic called LUMORA.
we want a clean design and the following informations: name of the doctor, doctor's registration number (called CRM), telephone, address, facebook, instagram.
Colors: white, blue tones, light brown/ coffee

facebook and instagram: lumoracirurgiaestetica

Industry/Entity Type

Business

Contact Information for Business Card

clean design

Font styles to use
Serif
Sans Serif
Other font styles liked:
• helvetica light

Colors
cee9f5
85cae6
85abd2
3276b5
cfeae6
cedeed
eaf1f7

Requirements
Must have
• doctor's name
• identification number (called CRM)
• contact (phone, facebook, instagram, address)

```html
<!DOCTYPE html>
<html lang="pt">
<head>
<meta charset="utf-8">
<title>Lumora – Business Card</title>
<link rel="stylesheet" href="https://fonts.googleapis.com/css2?family=Cinzel:wght@400;600;700&family=Arimo:wght@400&display=swap">
<style>
  :root{
    --navy:#173a66;
    --teal:#2bb5da;
    --white:#ffffff;
    --page:#e6ebf0;
    --muted:#cfe3f2;
  }
  *{box-sizing:border-box;margin:0;padding:0}
  html,body{width:1200px;height:900px;overflow:hidden;background:var(--page)}
  .sheet{position:relative;width:1200px;height:900px}
  .card{position:absolute;left:280px;width:640px;height:366px;border-radius:18px;overflow:hidden;
        box-shadow:0 6px 18px rgba(20,40,70,.18)}
  .card--back{top:58px;background:var(--navy)}
  .card--front{top:476px;background:var(--white)}

  /* brand */
  .brand{position:absolute;left:0;right:0;text-align:center}
  .brand__name{font-family:'Cinzel',serif;font-weight:400;color:var(--teal);letter-spacing:4px;line-height:1}
  .brand__sub{font-family:'Cinzel',serif;letter-spacing:2px;margin-top:6px}
  .card--back .brand{top:92px}
  .card--back .brand__name{font-size:80px}
  .card--back .brand__sub{font-size:26px;color:var(--white)}
  .brand__sub .tld{font-family:'Arimo',Helvetica,sans-serif;font-size:14px;color:var(--teal);letter-spacing:0}
  .web{position:absolute;bottom:34px;left:0;right:0;text-align:center;font-family:'Arimo',Helvetica,sans-serif;font-size:16px;color:var(--muted)}
  .web .lead{color:var(--teal)}

  /* front */
  .band{position:absolute;inset:0}
  .card--front .brand{top:26px}
  .card--front .brand__name{font-size:58px}
  .card--front .brand__sub{font-size:19px;color:var(--navy)}

  .name-row{position:absolute;top:143px;left:0;right:0;display:flex;align-items:center;gap:14px}
  .name-row .rule{height:2px;background:var(--navy)}
  .name-row .rule--l{width:128px}
  .name-row .rule--r{flex:1}
  .doctor{font-family:'Cinzel',serif;font-weight:700;font-size:23px;color:var(--navy);letter-spacing:1px}
  .doctor .title{color:var(--teal)}

  .contacts{position:absolute;top:180px;left:214px;list-style:none;font-family:'Arimo',Helvetica,sans-serif;font-size:13.5px;line-height:19px;color:var(--navy)}
  .contacts .label{color:var(--teal);display:inline-block;width:20px}
  .rule-low{position:absolute;top:254px;left:0;width:366px;height:2px;background:var(--navy)}

  .crm{position:absolute;top:272px;left:36px;font-family:'Arimo',Helvetica,sans-serif;font-size:15px;color:var(--navy)}
  .crm .key{color:var(--teal)}
  .address{position:absolute;top:324px;left:36px;display:flex;align-items:center;gap:12px;font-family:'Arimo',Helvetica,sans-serif;font-size:13.5px;line-height:18px;color:var(--white)}

  .social__dot{position:absolute;top:236px;right:16px;width:16px;height:16px;border-radius:50%;background:var(--teal)}
  .social{position:absolute;top:258px;right:16px;text-align:right;font-family:'Arimo',Helvetica,sans-serif;font-size:11px;line-height:19px;color:var(--white)}
</style>
</head>
<body>
<main class="sheet">

  <section class="card card--back" aria-label="Card back">
    <div class="brand">
      <div class="brand__name">LUMORA</div>
      <div class="brand__sub">Cirurgia Plástica<span class="tld">.com</span></div>
    </div>
    <p class="web"><span class="lead">www.</span>lumoracirurgiaestetica<span class="lead">.com</span></p>
  </section>

  <section class="card card--front" aria-label="Card front">
    <svg class="band" width="640" height="366" viewBox="0 0 640 366" aria-hidden="true">
      <path d="M0 318 H390 C418 318 418 226 446 226 H640 V366 H0 Z" fill="#173a66"/>
      <circle cx="410" cy="280" r="36" fill="#ffffff"/>
      <circle cx="410" cy="280" r="30" fill="#2bb5da"/>
    </svg>

    <div class="brand">
      <div class="brand__name">LUMORA</div>
      <div class="brand__sub">Cirurgia Plástica</div>
    </div>

    <div class="name-row">
      <span class="rule rule--l"></span>
      <h1 class="doctor"><span class="title">Dr.</span> Rafael Duarte</h1>
      <span class="rule rule--r"></span>
    </div>

    <ul class="contacts">
      <li><span class="label">P:</span> +330 5512-3097</li>
      <li><span class="label">E:</span> info@lumoracirurgiaestetica.com</li>
      <li><span class="label">W:</span> www.lumoracirurgiaestetica.com</li>
    </ul>
    <div class="rule-low"></div>

    <p class="crm"><span class="key">CRM</span>-58246</p>

    <div class="address">
      <svg width="24" height="22" viewBox="0 0 24 22" aria-hidden="true">
        <path d="M12 2 L1 11 H4 V20 H10 V14 H14 V20 H20 V11 H23 Z" fill="#2bb5da"/>
      </svg>
      <p>4715 Harbor Crest Way C<br>Palm Vale FL 33190</p>
    </div>

    <span class="social__dot" aria-hidden="true"></span>
    <p class="social">facebook/lumoracirurgiaestetica<br>@lumoracirurgiaestetica</p>
  </section>

</main>
</body>
</html>
```